Supplement Label Design - Sports Nutrition

Design a sports nutrition/weight loss supplement label that stands out in a crowded space. Supplement bottle size is 200c and label size is 7" x 2.5" approximately. We're looking for a design that emphasizes the products name called VYK. Vyk is an abbreviation for Vigor, Yield & Kinetics. We want VYK to be the center/focus point of the bottle and have a memorable design to it.

Target Market(s)

Men & Women over 18

Industry/Entity Type

Supplement

Font styles to use
Sans Serif
Decorative

Requirements
Must have
• Emphasis on the product name VYK. Serious, Inspirational & Motivational feel to the design, typo & colors. Electrocution/lightning feel to the text. Right hand side of label is our formulation. Left hand side is dedicated to explaining the trifecta formulation idea.
Nice to have
• For example, we like the graphic design of "Drum" energy drinks because you can identify the bottle from a distance and is memorable. We think that less is more and we'd like the design/colors do most of the talking.
Should not have
• Cartroon/animated style.

```html
<!DOCTYPE html>
<html lang="en">
<head>
<meta charset="utf-8">
<title>VYK – Supplement Label</title>
<link rel="stylesheet" href="https://fonts.googleapis.com/css2?family=Montserrat:wght@600;900&family=Open+Sans:ital,wght@0,400;0,700;1,400&display=swap">
<style>
  :root {
    --brand-pink: #d01e5e;
    --ink: #222222;
    --paper: #ffffff;
    --rule: #4a4a4a;
    --label-font: "Open Sans", Arial, sans-serif;
    --brand-font: "Montserrat", Arial, sans-serif;
    --note-font: Arial, Helvetica, sans-serif;
  }
  html, body {
    margin: 0;
    padding: 0;
    width: 1200px;
    height: 429px;
    overflow: hidden;
    background: var(--paper);
  }
  .label {
    position: relative;
    width: 1200px;
    height: 429px;
    overflow: hidden;
    background: var(--paper);
  }
  .artwork {
    position: absolute;
    inset: 0;
  }
  .brand-name {
    font-family: var(--brand-font);
    font-weight: 900;
    fill: var(--ink);
  }
  .brand-tagline {
    font-family: var(--brand-font);
    font-weight: 600;
    fill: var(--ink);
  }

  .facts {
    position: absolute;
    left: 727px;
    top: 50px;
    width: 448px;
    border: 2px solid #000;
    background: var(--paper);
    font-family: var(--label-font);
    font-size: 9.2px;
    color: #111;
    line-height: 1;
  }
  .facts-head {
    height: 54px;
    position: relative;
  }
  .facts-title {
    position: absolute;
    left: 3px;
    top: 7px;
    font-size: 13.8px;
    font-weight: 700;
  }
  .facts-serving { position: absolute; left: 3px; top: 28px; }
  .facts-count { position: absolute; left: 3px; top: 43px; }

  .row {
    position: relative;
    height: 14px;
    border-top: 1px solid var(--rule);
    box-sizing: border-box;
    padding-left: 3px;
    line-height: 13px;
    white-space: nowrap;
  }
  .row.thick-top { border-top: 2px solid #000; line-height: 12px; }
  .row.blend { font-weight: 700; }
  .row.blend .dv { font-weight: 400; }
  .row.sub { padding-left: 10px; }
  .row .amt, .row .unit, .row .dv {
    position: absolute;
    top: 0;
    width: 34px;
    text-align: center;
  }
  .row .amt { left: 304px; }
  .row .unit { left: 357px; }
  .row .dv { left: 409px; }
  .row.footnote { height: 15px; }

  .other-ingredients,
  .warning {
    position: absolute;
    left: 730px;
    margin: 0;
    font-family: var(--note-font);
    font-size: 9.2px;
    line-height: 1;
    color: #111;
  }
  .other-ingredients { top: 347px; }
  .warning { top: 376px; font-weight: 700; }
</style>
</head>
<body>
<main class="label">
  <svg class="artwork" width="1200" height="429" viewBox="0 0 1200 429" aria-hidden="true">
    <circle class="corner-ring" cx="-23" cy="26" r="155" fill="none" stroke="var(--brand-pink)" stroke-width="56"/>
    <path class="formula-arc" d="M 1025.4 54.5 A 257 257 0 1 0 1074.9 430.2" fill="none" stroke="var(--brand-pink)" stroke-width="106"/>
    <text class="brand-name" x="192" y="388" font-size="112" textLength="216" lengthAdjust="spacingAndGlyphs">VYK</text>
    <text class="brand-tagline" x="192" y="406" font-size="13.5" textLength="214" lengthAdjust="spacingAndGlyphs">VIGOR, YIELD &amp; KINETICS</text>
  </svg>

  <section class="facts" aria-label="Supplement Facts">
    <div class="facts-head">
      <div class="facts-title">Supplement Facts</div>
      <div class="facts-serving">Serving Size: 2 capsules</div>
      <div class="facts-count">Servings Per Container: 30</div>
    </div>
    <div class="row">Amount per Serving<span class="dv">%DV</span></div>
    <div class="row thick-top">Niacin (as niacinamide)<span class="amt">40</span><span class="unit">mg</span><span class="dv">250%</span></div>
    <div class="row">Vitamin B6 (as pyridoxal-5-phosphate)<span class="amt">8.5</span><span class="unit">mg</span><span class="dv">500%</span></div>
    <div class="row">Vitamin B12 (as methylcobalamin)<span class="amt">12</span><span class="unit">mcg</span><span class="dv">500%</span></div>
    <div class="row thick-top blend">Proprietary Zen Blend<span class="amt">450</span><span class="unit">mg</span><span class="dv">*</span></div>
    <div class="row sub">Ashwagandha Root Extract (<i>Withania somnifera</i>)<span class="dv">*</span></div>
    <div class="row sub">Acetyl L-Carnitine HCl<span class="dv">*</span></div>
    <div class="row sub">L-Theanine<span class="dv">*</span></div>
    <div class="row blend">Proprietary Appetite Blend<span class="amt">425</span><span class="unit">mg</span><span class="dv">*</span></div>
    <div class="row sub"><i>Garcinia cambogia</i> extract (fruit)<span class="dv">*</span></div>
    <div class="row sub">Yohimbe Bark Extract (<i>Pausinystalia johimbe</i>)<span class="dv">*</span></div>
    <div class="row sub">Capsirex® (capsicum fruit extract)(standardized to 2% capsaicinoids)</div>
    <div class="row blend">Proprietary Performance Blend (215 mg Caffiene)<span class="amt">320</span><span class="unit">mg</span><span class="dv">*</span></div>
    <div class="row sub">Green Tea Extract<span class="dv">*</span></div>
    <div class="row sub">Theobromine<span class="dv">*</span></div>
    <div class="row sub">Green Coffee Fruit Extract<span class="dv">*</span></div>
    <div class="row thick-top footnote">*Daily Value (DV) not established</div>
  </section>

  <p class="other-ingredients">Other Ingredients: Rice flour, L-leucine, hypromellose (capsule).</p>
  <p class="warning">Warning: Contains 215 mg of caffeine per serving.</p>
</main>
</body>
</html>
```